"Slipwise Forms" Cartvane Add-on Market Banner

Hey Designers! I need a photoshop banner to feature our web application, for use in the Cartvane Add-on Market. See http://addons.cartvane-example.com for examples of the other apps and their designs.
The image should be 310px wide x 100px tall. Suggested colors should be taken from our homepage: http://shop.slipwiseforms-example.com/ and are also suggested below.
At minimum, the app banner must contain the name "Slipwise Forms".
The application itself provides people with printable customized Invoice, Packing Slips templates, so imagery should reflect that in some way. Perhaps a printer or document icon for imagery.
I prefer flat design, or simple design without too much clutter or small details.
Target Market(s)
Adults based in United States, UK and Australia.. aged 25-35 who run online e-commerce businesses through Cartvane.com
Industry/Entity Type
Printer
Requirements
Must have
- The words "Slipwise Forms".
Black background, grey and white details.
Nice to have
- illustration style images, in flat design style if possible.
I like this type of design style: http://gridloft-example.com/tour/overview/
Should not have
- Photo like images.
White background.

```html
<!DOCTYPE html>
<html lang="en">
<head>
<meta charset="utf-8">
<title>Slipwise Forms – Add-on Market Banners</title>
<link href="https://fonts.googleapis.com/css2?family=PT+Sans:wght@400;700&display=swap" rel="stylesheet">
<style>
  :root {
    --page: #ffffff;
    --banner-blue: #4a9bd8;
    --banner-green: #55bb68;
    --banner-charcoal: #444444;
    --title: #f4f4f4;
    --tagline: #ffffff;
    --printer-yellow: #f9d12a;
    --printer-orange: #f5922a;
  }
  html, body {
    margin: 0;
    padding: 0;
    width: 1200px;
    height: 674px;
    overflow: hidden;
    background: var(--page);
    font-family: "PT Sans", sans-serif;
  }
  .sheet {
    position: relative;
    width: 1200px;
    height: 674px;
  }
  .banner {
    position: absolute;
    overflow: hidden;
    color: var(--title);
  }
  .banner--hero {
    left: 61px; top: 58px; width: 1081px; height: 347px;
    background: var(--banner-blue);
  }
  .banner--green {
    left: 61px; top: 461px; width: 496px; height: 158px;
    background: var(--banner-green);
  }
  .banner--charcoal {
    left: 640px; top: 461px; width: 498px; height: 158px;
    background: var(--banner-charcoal);
  }
  .banner__title {
    position: absolute;
    margin: 0;
    font-weight: 700;
    line-height: 0.98;
    letter-spacing: -0.5px;
  }
  .banner__tagline {
    position: absolute;
    margin: 0;
    font-weight: 400;
    line-height: 1.05;
    color: var(--tagline);
  }
  .banner__art {
    position: absolute;
    border-radius: 10px;
    background: linear-gradient(160deg, var(--printer-yellow) 0%, var(--printer-yellow) 45%, var(--printer-orange) 100%);
  }

  .banner--hero .banner__title { left: 92px; top: 44px; font-size: 74px; }
  .banner--hero .banner__tagline { left: 110px; top: 222px; font-size: 38px; }
  .banner--hero .banner__art { left: 680px; top: 33px; width: 246px; height: 269px; }

  .banner--small .banner__title { left: 41px; top: 22px; font-size: 35px; }
  .banner--small .banner__tagline { left: 49px; top: 98px; font-size: 18px; }
  .banner--small .banner__art { left: 310px; top: 14px; width: 133px; height: 130px; border-radius: 6px; }
</style>
</head>
<body>
<main class="sheet">

  <section class="banner banner--hero">
    <h1 class="banner__title">Slipwise<br>Forms</h1>
    <p class="banner__tagline">Professional Designs<br>without the headaches!</p>
    <div class="banner__art" role="img" aria-label="Flat yellow and orange printer illustration with a sheet of paper and a long shadow"></div>
  </section>

  <section class="banner banner--small banner--green">
    <h2 class="banner__title">Slipwise<br>Forms</h2>
    <p class="banner__tagline">Professional Designs<br>without the headaches!</p>
    <div class="banner__art" role="img" aria-label="Flat yellow and orange printer illustration with a sheet of paper and a long shadow"></div>
  </section>

  <section class="banner banner--small banner--charcoal">
    <h2 class="banner__title">Slipwise<br>Forms</h2>
    <p class="banner__tagline">Professional Designs<br>without the headaches!</p>
    <div class="banner__art" role="img" aria-label="Flat yellow and orange printer illustration with a sheet of paper and a long shadow"></div>
  </section>

</main>
</body>
</html>
```